Brochure Design Project

We need a brochure for our acting school, website is
www.stagelanternhouse.com - It needs to reflect youth, vitality, and people's DREAMS coming true...colors should be red and black, but open to something new as well...the courses included should be
Players' Spark Week, Rising Talent Bundle, And The Mastery Track

Emphasis on Players' Spark Week is the short term intensity.
Rising Talent Bundle is the benefit of getting all the tools to look for acting work.
Mastery Track is becoming a pro, and if you are in another country, being provided with a visa to come to the U.S.

I have attached pictures and logos...I will submit the copy once there is a framework...the OLD brochure is attached as well...

Thank you...

Harold

Reason: We would like to see a couple more ideas...

Reason: HI there designers! Thanks for your submissions. We are almost ready to pick a design. Thanks for the understanding.

Target Market(s)

18-35 year olds...fairly affluent, educated, American, European, or Australian

Industry/Entity Type

School

Requirements
Must have
• Make it fun, clean, clear, and NOT corporate.

```html
<!DOCTYPE html>
<html lang="en">
<head>
<meta charset="utf-8">
<title>Stage Lantern House – The Programs</title>
<link rel="stylesheet" href="https://fonts.googleapis.com/css2?family=Didact+Gothic&family=Crimson+Text:wght@400&family=Indie+Flower&display=swap">
<style>
:root{
  --maroon:#5e1214;
  --maroon-light:#6e1719;
  --red:#8b1d20;
  --black:#000;
  --yellow:#fff200;
  --yellow-text:#f4e400;
  --grey:#4d4d4f;
  --white:#fff;
  --ink:#111;
}
*{margin:0;padding:0;box-sizing:border-box}
html,body{width:1200px;height:927px;overflow:hidden;background:var(--black)}
.brochure{position:relative;width:1200px;height:927px;font-family:"Didact Gothic",sans-serif;color:var(--white)}

.intro{position:absolute;left:0;top:0;width:400px;height:927px;background:linear-gradient(180deg,var(--maroon-light),var(--maroon) 60%,#4e0e10)}
.intro .brush{position:absolute;left:20px;top:50px;width:338px;height:78px;background:var(--black);border-radius:3px 36px 8px 24px}
.intro h1{position:absolute;left:34px;top:52px;font-weight:400;font-size:37px;line-height:36px;letter-spacing:.2px;white-space:nowrap}
.intro h1 .dream{color:var(--yellow)}
.intro .quote{position:absolute;left:34px;top:148px;width:335px;font-family:"Indie Flower",cursive;font-size:22px;line-height:26px;letter-spacing:.8px;color:#f2f2f2}
.intro .quote em{font-style:normal;color:var(--yellow-text)}
.intro .body{position:absolute;left:34px;width:345px;font-size:16.4px;line-height:19.6px;color:#f0f0f0}
.intro .p1{top:375px}
.intro .p2{top:532px}
.signature{position:absolute;left:38px;top:764px;width:280px;height:40px;background:linear-gradient(90deg,rgba(255,255,255,.18),rgba(255,255,255,.04))}
.sign-name{position:absolute;left:34px;top:820px;font-size:16.4px;line-height:20px;color:#f0f0f0}

.top-band{position:absolute;left:400px;top:0;width:800px;height:80px;background:var(--red)}
.top-band h2{position:absolute;right:25px;top:27px;font-weight:400;font-size:31px;letter-spacing:.5px}

.photo{position:absolute;left:400px;top:440px;width:800px;height:487px;
  background:
    radial-gradient(ellipse 260px 170px at 48% 48%,rgba(196,150,120,.75),rgba(196,150,120,0)),
    radial-gradient(ellipse 220px 150px at 75% 35%,rgba(170,125,95,.7),rgba(170,125,95,0)),
    radial-gradient(ellipse 200px 140px at 25% 62%,rgba(150,110,85,.65),rgba(150,110,85,0)),
    radial-gradient(ellipse 240px 130px at 72% 70%,rgba(90,90,60,.6),rgba(90,90,60,0)),
    radial-gradient(ellipse at 60% 55%,#3a2c24 0%,#1a1410 55%,#050505 85%)}

.brand{position:absolute;left:600px;top:56px;width:180px;text-align:center;font-size:20px;line-height:20px;letter-spacing:.5px;color:var(--white);z-index:3}
.brand .mark{display:inline-block;width:9px;height:9px;background:var(--white);margin-left:5px;vertical-align:top}

.card{position:absolute;border-radius:14px;padding:12px 16px 12px 20px}
.card h3{font-weight:400;font-size:18px;line-height:19px;text-transform:uppercase}
.card p{font-family:"Crimson Text",serif;font-size:15.2px;line-height:18.5px}
.card h3 + p{margin-top:3px}
.card.basic{left:425px;top:98px;width:358px;height:228px;background:var(--yellow);color:var(--ink);padding:15px 14px 12px 20px}
.card.basic h3{font-size:21px;line-height:19px}
.card.basic .tag{font-family:"Indie Flower",cursive;font-size:17px;line-height:18px;letter-spacing:.3px;margin:10px 0 8px}
.card.grey{background:var(--grey);color:var(--white)}
.card.battle{left:400px;top:314px;width:355px;height:128px;border-radius:0 14px 14px 0;padding-left:26px}
.card.bundle{left:818px;top:98px;width:357px;height:114px}
.card.advanced{left:838px;top:202px;width:362px;height:125px;background:var(--white);color:var(--ink);border-radius:14px 0 0 14px;padding:13px 8px 12px 17px}
.card.mastery{left:800px;top:318px;width:340px;height:125px;padding:15px 8px 12px 18px}
.card.mastery p{font-size:14.8px}

.notice{position:absolute;left:422px;top:452px;width:302px;height:122px;z-index:2}
.notice svg{position:absolute;left:0;top:0}
.notice p{position:absolute;left:46px;top:35px;width:210px;text-align:center;font-size:13.6px;line-height:16px;color:var(--white)}
</style>
</head>
<body>
<main class="brochure">
  <section class="intro">
    <div class="brush"></div>
    <h1><span class="dream">YOUR DREAMS</span><br>START HERE</h1>
    <p class="quote">Whatever you wind up doing with your life, like it or not, at some point you will look back on that occupation and call it your life's work. <em>So choose wisely. And if that doesn't work, choose acting.</em></p>
    <p class="body p1">Because quite honestly, acting is not the pragmatic choice, it is so much more. It is a choice based on a dream, an inexplicable desire to experience and express the human condition and to do all that in front of others. And hopefully for hard currency. Not a bad way to spend one's time on this planet.</p>
    <p class="body p2">It is in the service of this idea that Stage Lantern House was born. Our approach is simple: you act in every single class-extensively, you learn from active working professionals, and then you are assisted and encouraged to get out in the real world and get a job. That's right, a job - an acting job. Because after all we are here to get actors acting, end of story.</p>
    <div class="signature" role="img" aria-label="Handwritten signature of Harold Marsh"></div>
    <p class="sign-name">Harold Marsh<br>Founder and Artistic Director</p>
  </section>

  <header class="top-band"><h2>THE PROGRAMS</h2></header>

  <div class="photo" role="img" aria-label="Group photo of cheerful acting students piled together on a dark stage"></div>

  <div class="brand">PLAYERS'<br>SPARK WEEK<span class="mark"></span></div>

  <article class="card basic">
    <h3>Basic<br>Training</h3>
    <p class="tag">"Is this acting thing just a passing fancy or is it truly my life's work?"</p>
    <p>By the end of this truly intensive course, you will not only know the answer to the former question, but you will have the cornerstone of a strong foundation in acting technique as well as its application to scene work and cold readings.</p>
  </article>

  <article class="card grey battle">
    <h3 style="text-transform:none">PLAYERS' SPARK WEEK II – Into Battle</h3>
    <p>Here you will learn true on-camera skills so that you can work on any type of shoot, and you will learn and apply business tools that will get you going in your career.</p>
  </article>

  <article class="card grey bundle">
    <h3>The Rising Talent Bundle</h3>
    <p>Spark Week I and II back to back, giving you everything you need to book the part, including a personalized way to market yourself.</p>
  </article>

  <article class="card advanced">
    <h3>The Advanced Program</h3>
    <p>You will gain a deep understanding of character and script analysis, as well as invaluable experience playing many different kinds of parts in all of the genres you might audition for in today's industry.</p>
  </article>

  <article class="card grey mastery">
    <h3>The Mastery Track</h3>
    <p>Designed for actors who come to Los Angeles and are committed to turning their dreams into reality, the 9 month Mastery Track gets you working on your acting 22 hours a week, every week.</p>
  </article>

  <div class="notice">
    <svg width="302" height="122" viewBox="0 0 302 122" aria-hidden="true">
      <ellipse cx="151" cy="60" rx="144" ry="52" fill="none" stroke="#fff200" stroke-width="7"/>
      <ellipse cx="149" cy="58" rx="137" ry="47" fill="none" stroke="#fff200" stroke-width="2"/>
    </svg>
    <p>This school is authorized under federal law to enroll non-immigrant alien students</p>
  </div>
</main>
</body>
</html>
```